Customer Dashboard Design for Email Security SaaS

Mailbrook is a commercial email spam filter offered as a SaaS product, built and operated by a small German hosting provider. It protects business email accounts against spam, phishing, scam, and viruses using a multilayer filtering pipeline that combines traditional spam detection with AI-powered classification. The product runs entirely on German infrastructure, ensuring data sovereignty for European customers.

We need a complete redesign of the customer-facing dashboard. This is the web application where paying customers manage their email filtering: view their mail log, check quarantined emails, manage allow/blocklists, configure their settings, and handle their subscription. It is the primary touchpoint between Mailbrook and its customers.

Our customers are system administrators, IT managers at small-to-medium businesses, and operators of small hosting providers. They are technically competent but not designers. They expect professional, efficient tools that respect their time. They typically manage 10–500 email accounts and check the dashboard a few times per week, with heavier use during spam incidents.

We have attached the current mockups which really need to be replaced with something good looking.

Target Market(s)

System administrators, IT managers at small-to-medium businesses, and operators of small hosting providers.

Industry/Entity Type

SaaS

Number of Pages Required

5+ page

```html
<!DOCTYPE html>
<html lang="en">
<head>
<meta charset="utf-8">
<title>Mailbrook – Settings</title>
<link href="https://fonts.googleapis.com/css2?family=Poppins:wght@400;500;600;700&display=swap" rel="stylesheet">
<style>
:root{
  --bg:#1b1a1a;
  --panel:#211f1f;
  --panel-border:#2c2a2a;
  --field:#363535;
  --green:#0e9a6b;
  --green-dark:#0b4a36;
  --text:#ffffff;
  --muted:#cfcfcf;
  --placeholder:#8a8a8a;
  --admin:#3a3838;
}
*{box-sizing:border-box;margin:0;padding:0}
html,body{width:1200px;height:750px;overflow:hidden;background:var(--bg);font-family:"Poppins",sans-serif;color:var(--text)}
.app{position:relative;width:1200px;height:750px}

/* Sidebar */
.sidebar{position:absolute;left:17px;top:15px;width:199px;height:721px;background:var(--panel);border:1px solid var(--panel-border);border-radius:25px}
.brand{position:absolute;left:0;top:27px;width:100%;text-align:center}
.brand-mark{width:45px;height:45px;margin:0 auto;background:var(--green);border-radius:10px}
.brand-name{margin-top:8px;font-size:22.5px;font-weight:500;letter-spacing:-.2px}
.nav{position:absolute;left:0;top:0;width:100%;list-style:none}
.nav-item{position:absolute;left:33px;display:flex;align-items:center;gap:11px;font-size:10.6px;color:var(--text);transform:translateY(-50%)}
.nav-item svg{width:16px;height:16px;stroke:#9a9a9a;fill:none;stroke-width:1.4}
.nav-item.active{left:19px;width:161px;height:40px;background:var(--green);border-radius:12px;padding-left:14px;transform:none}
.nav-item.active svg{stroke:#fff}
.nav-item.active .chev{position:absolute;right:14px;width:10px;height:10px;stroke-width:2}
.divider{position:absolute;left:19px;top:607px;width:161px;height:1px;background:var(--panel-border)}
.section-label{position:absolute;left:0;top:628px;width:100%;text-align:center;font-size:9.4px;font-weight:600;letter-spacing:.3px}
.admin-btn{position:absolute;left:19px;top:648px;width:161px;height:40px;background:var(--admin);border-radius:12px;display:flex;align-items:center;justify-content:center;gap:6px;font-size:9.4px;font-weight:600;letter-spacing:.2px}

/* Header */
.page-icon{position:absolute;left:261px;top:42px;width:45px;height:45px;border:1px solid var(--panel-border);border-radius:10px;display:flex;align-items:center;justify-content:center}
.page-title{position:absolute;left:320px;top:34px;font-size:24px;font-weight:600}
.page-sub{position:absolute;left:321px;top:70px;font-size:11.3px;color:var(--muted)}
.theme-toggle{position:absolute;left:1106px;top:41px;width:49px;height:27px;background:#fff;border-radius:14px}
.theme-toggle .knob{position:absolute;left:3px;top:3px;width:21px;height:21px;border-radius:50%;background:#1b1a1a;display:flex;align-items:center;justify-content:center}
.theme-toggle .sun{position:absolute;right:5px;top:6px}

/* Profile */
.profile-card{position:absolute;left:261px;top:103px;width:200px;height:221px;border:1px solid var(--panel-border);border-radius:25px;background:var(--bg)}
.avatar{position:absolute;left:52px;top:32px;width:96px;height:96px;border-radius:50%;background:radial-gradient(circle at 50% 40%,#c8b6a4,#8e7a6a 60%,#d9d9d9 100%)}
.avatar-edit{position:absolute;left:117px;top:105px;width:25px;height:25px;border-radius:50%;background:var(--green);border:2px solid var(--bg);display:flex;align-items:center;justify-content:center}
.profile-name{position:absolute;left:0;top:144px;width:100%;text-align:center;font-size:17px;font-weight:700}
.profile-email{position:absolute;left:0;top:168px;width:100%;text-align:center;font-size:9.6px;color:var(--muted)}

/* Settings card */
.settings-card{position:absolute;left:474px;top:103px;width:681px;height:552px;background:var(--panel);border:1px solid var(--panel-border);border-radius:25px}
.settings-card > *{position:absolute}
.card-title{left:25px;top:20px;font-size:11.3px;font-weight:600}
.field-label{left:26px;font-size:9.4px;font-weight:500}
.field-label .req{color:var(--green)}
.field{left:26px;width:629px;height:33px;background:var(--field);border-radius:8px;display:flex;align-items:center;justify-content:space-between;padding:0 17px;color:var(--placeholder);font-size:10px;letter-spacing:1px}
.btn{background:var(--green);border-radius:8px;display:flex;align-items:center;justify-content:center;font-size:8px;font-weight:700;letter-spacing:.2px;color:#fff}
.update-btn{left:26px;top:242px;width:129px;height:37px}
.section-title{left:25px;font-size:12px;font-weight:500}
.range-value{right:26px;top:306px;font-size:9.4px}
.range{left:26px;top:333px;width:630px;height:4px;background:#fff;border-radius:2px}
.range-fill{position:absolute;left:0;top:0;width:287px;height:4px;background:var(--green);border-radius:2px}
.range-thumb{position:absolute;left:282px;top:-3px;width:10px;height:10px;border-radius:50%;background:var(--green)}
.select{letter-spacing:0}
.options{left:26px;top:477px;width:630px;height:45px;display:flex;gap:8px}
.option{flex:1;border:1px solid #1f3a31;border-radius:7px;background:linear-gradient(90deg,#12382b,#1b2622);padding:9px 15px}
.option-title{font-size:9.8px;font-weight:600}
.option-desc{font-size:8.8px;color:var(--muted);margin-top:2px}
.save-btn{position:absolute;left:473px;top:677px;width:124px;height:41px}
</style>
</head>
<body>
<div class="app">
  <aside class="sidebar">
    <div class="brand">
      <div class="brand-mark"></div>
      <div class="brand-name">Mailbrook</div>
    </div>
    <ul class="nav">
      <li class="nav-item" style="top:159px"><svg viewBox="0 0 16 16"><path d="M2 8 8 2.5 14 8M4 6.5V14h8V6.5M6.5 14v-4h3v4"/></svg>Dashboard</li>
      <li class="nav-item" style="top:192px"><svg viewBox="0 0 16 16"><path d="M2 3.5h1M5 3.5h9M2 6.5h1M5 6.5h9M2 9.5h1M5 9.5h9M2 12.5h1M5 12.5h9"/></svg>Mail Log</li>
      <li class="nav-item" style="top:224px"><svg viewBox="0 0 16 16"><rect x="1.5" y="3" width="13" height="10" rx="1.5"/><path d="m2 4 6 5 6-5"/></svg>Mailboxes</li>
      <li class="nav-item" style="top:257px"><svg viewBox="0 0 16 16"><path d="M8 1.5 13.5 3.5v4c0 3.5-2.5 5.8-5.5 7-3-1.2-5.5-3.5-5.5-7v-4Z"/><path d="m5.5 8 2 2 3-3.5"/></svg>Allowlist</li>
      <li class="nav-item" style="top:291px"><svg viewBox="0 0 16 16"><path d="M8 1.5 13.5 3.5v4c0 3.5-2.5 5.8-5.5 7-3-1.2-5.5-3.5-5.5-7v-4Z"/><path d="M8 5v3.5M8 10.5v.5"/></svg>Blocklist</li>
      <li class="nav-item" style="top:325px"><svg viewBox="0 0 16 16"><rect x="3" y="7" width="10" height="7.5" rx="1.5"/><path d="M5 7V5a3 3 0 0 1 5.8-1M8 10v2"/></svg>Quarantine</li>
      <li class="nav-item active" style="top:345px"><svg viewBox="0 0 16 16"><circle cx="8" cy="8" r="2.3"/><path d="M8 1.5 9.2 3l1.9-.4.6 1.8 1.8.6-.4 1.9L14.5 8 13.1 9.2l.4 1.9-1.8.6-.6 1.8-1.9-.4L8 14.5 6.8 13.1l-1.9.4-.6-1.8-1.8-.6.4-1.9L1.5 8l1.4-1.2-.4-1.9 1.8-.6.6-1.8 1.9.4Z"/></svg>Settings<svg class="chev" viewBox="0 0 10 10"><path d="m3.5 2 3 3-3 3"/></svg></li>
      <li class="nav-item" style="top:411px"><svg viewBox="0 0 16 16"><rect x="7" y="8" width="7.5" height="6.5" rx="1"/><path d="M9 10.5h3.5M9 12.5h3.5M6 14.5H2.5c0-4 1.5-6 3.5-7M4.5 5 3.5 2.5h4L6.5 5Z"/></svg>Billing</li>
    </ul>
    <div class="divider"></div>
    <div class="section-label">VERWALTUNG</div>
    <div class="admin-btn"><svg width="11" height="11" viewBox="0 0 12 12" fill="#fff"><circle cx="6" cy="3.2" r="2.7"/><path d="M1 12c0-3 2.2-5 5-5s5 2 5 5Z"/></svg>ADMINISTRATION</div>
  </aside>

  <header>
    <div class="page-icon"><svg width="21" height="21" viewBox="0 0 16 16" fill="none" stroke="#fff" stroke-width="1.1"><circle cx="8" cy="8" r="2.3"/><path d="M8 1.5 9.2 3l1.9-.4.6 1.8 1.8.6-.4 1.9L14.5 8 13.1 9.2l.4 1.9-1.8.6-.6 1.8-1.9-.4L8 14.5 6.8 13.1l-1.9.4-.6-1.8-1.8-.6.4-1.9L1.5 8l1.4-1.2-.4-1.9 1.8-.6.6-1.8 1.9.4Z"/></svg></div>
    <h1 class="page-title">Settings</h1>
    <p class="page-sub">Manage your account and filtering behavior</p>
    <div class="theme-toggle">
      <div class="knob"><svg width="12" height="12" viewBox="0 0 12 12" fill="none" stroke="#fff" stroke-width="1.1"><path d="M9.5 7.5A4 4 0 0 1 4.5 2.5a4 4 0 1 0 5 5Z"/></svg></div>
      <svg class="sun" width="14" height="14" viewBox="0 0 14 14" fill="none" stroke="#1b1a1a" stroke-width="1.1"><circle cx="7" cy="7" r="2.6"/><path d="M7 .8v1.6M7 11.6v1.6M.8 7h1.6M11.6 7h1.6M2.6 2.6l1.1 1.1M10.3 10.3l1.1 1.1M2.6 11.4l1.1-1.1M10.3 3.7l1.1-1.1"/></svg>
    </div>
  </header>

  <section class="profile-card">
    <div class="avatar" role="img" aria-label="Profile photo of the account holder"></div>
    <div class="avatar-edit"><svg width="11" height="11" viewBox="0 0 12 12" fill="none" stroke="#fff" stroke-width="1.2"><path d="M8 1.5 10.5 4 4 10.5H1.5V8Z"/></svg></div>
    <div class="profile-name">Lena Marwitz</div>
    <div class="profile-email">lena.marwitz@mailbrook-demo.de</div>
  </section>

  <section class="settings-card">
    <h2 class="card-title">Change Password</h2>
    <label class="field-label" style="top:52px">Current password<span class="req">*</span></label>
    <div class="field" style="top:73px">**************<svg width="15" height="15" viewBox="0 0 16 16" fill="none" stroke="#fff" stroke-width="1.5"><path d="M1 8s2.5-4.5 7-4.5S15 8 15 8s-2.5 4.5-7 4.5S1 8 1 8Z"/><circle cx="8" cy="8" r="2"/><path d="M2.5 2.5l11 11"/></svg></div>
    <label class="field-label" style="top:112px">New password<span class="req">*</span></label>
    <div class="field" style="top:133px">**************<svg width="15" height="15" viewBox="0 0 16 16" fill="none" stroke="#fff" stroke-width="1.5"><path d="M1 8s2.5-4.5 7-4.5S15 8 15 8s-2.5 4.5-7 4.5S1 8 1 8Z"/><circle cx="8" cy="8" r="2"/><path d="M2.5 2.5l11 11"/></svg></div>
    <label class="field-label" style="top:172px">Confirm New password<span class="req">*</span></label>
    <div class="field" style="top:193px">**************<svg width="15" height="15" viewBox="0 0 16 16" fill="none" stroke="#fff" stroke-width="1.5"><path d="M1 8s2.5-4.5 7-4.5S15 8 15 8s-2.5 4.5-7 4.5S1 8 1 8Z"/><circle cx="8" cy="8" r="2"/><path d="M2.5 2.5l11 11"/></svg></div>
    <div class="btn update-btn">UPDATE PASSWORD</div>

    <h3 class="section-title" style="top:310px">Retention Period</h3>
    <span class="range-value">30 days</span>
    <div class="range"><div class="range-fill"></div><div class="range-thumb"></div></div>

    <h3 class="section-title" style="top:364px;left:26px">Anonymization Period</h3>
    <div class="field select" style="top:388px">30<svg width="10" height="10" viewBox="0 0 10 10" fill="none" stroke="#fff" stroke-width="1.5"><path d="m2 3.5 3 3 3-3"/></svg></div>

    <h3 class="section-title" style="top:449px">Oversize Email Behavior</h3>
    <div class="options">
      <div class="option"><div class="option-title">Block</div><div class="option-desc">Reject the email completely</div></div>
      <div class="option"><div class="option-title">Quarantine</div><div class="option-desc">Hold the email for manual review</div></div>
      <div class="option"><div class="option-title">Deliver Anyway</div><div class="option-desc">Allow email despite size limit</div></div>
    </div>
  </section>

  <div class="btn save-btn">SAVE SETTINGS</div>
</div>
</body>
</html>
```